Vendrick Contracting Service Flyer

We are looking to have a one page flyer designed for our services that we do
We want to keep the same colors as our logo

Requirements
Must have
• Our Name should be in Onyx Font
• Colors Used:
• 070bac
• b3b4e6
• fbd234

```html
<!DOCTYPE html>
<html lang="en">
<head>
<meta charset="utf-8">
<title>Vendrick Contracting – Our Services</title>
<link href="https://fonts.googleapis.com/css2?family=Playfair+Display:wght@700&family=Arimo:ital,wght@0,400;1,400;1,700&display=swap" rel="stylesheet">
<style>
  :root {
    --brand-blue: #070bac;
    --brand-lavender: #b3b4e6;
    --brand-yellow: #fbd234;
    --paper: #ffffff;
  }
  * { margin: 0; padding: 0; box-sizing: border-box; }
  html, body { width: 778px; height: 1200px; overflow: hidden; background: var(--paper); }
  .flyer { position: relative; width: 778px; height: 1200px; background: var(--paper); overflow: hidden; font-family: "Arimo", sans-serif; }

  .brand { position: absolute; top: 36px; left: 0; width: 100%; text-align: center; color: var(--brand-blue); font-family: "Playfair Display", serif; font-weight: 700; }
  .brand-name { display: block; font-size: 80px; line-height: 1; letter-spacing: 4px; }
  .brand-sub { display: block; font-size: 42px; line-height: 1.2; margin-top: 10px; }

  .edge-strip { position: absolute; top: 222px; left: 0; width: 10px; height: 978px; background: var(--brand-lavender); }
  .top-strip { position: absolute; top: 222px; left: 0; width: 100%; height: 14px; background: var(--brand-lavender); }

  .services-band { position: absolute; top: 236px; left: 0; width: 100%; height: 112px; background: var(--brand-blue); }
  .services-title { position: absolute; left: 30px; top: 14px; color: var(--brand-yellow); font-family: "Playfair Display", serif; font-weight: 700; font-size: 72px; line-height: 1; transform: scaleX(0.82); transform-origin: left center; }
  .services-rule { position: absolute; left: 428px; top: 78px; width: 350px; height: 7px; background: var(--brand-yellow); }

  .service-list { position: absolute; left: 36px; top: 394px; list-style: none; color: var(--brand-blue); font-style: italic; font-size: 20px; line-height: 27.3px; }
  .service-list .gap { height: 27.3px; }

  .photo-rail { position: absolute; left: 456px; top: 376px; width: 11px; height: 661px; background: var(--brand-yellow); }
  .photo { position: absolute; left: 467px; width: 311px; }
  .photo-saw { top: 376px; height: 196px; background: linear-gradient(135deg, #efe6dc 0%, #c9a27a 55%, #7c5a3c 100%); }
  .photo-tower { top: 576px; height: 232px; background: linear-gradient(160deg, #7fb2d9 0%, #2f5f8a 55%, #0d2440 100%); }
  .photo-floor { top: 812px; height: 225px; background: linear-gradient(180deg, #4b4b4b 0%, #8a7a68 55%, #c9b69a 100%); }

  .contact-bar { position: absolute; top: 1037px; left: 0; width: 100%; height: 80px; background: var(--brand-lavender); display: flex; align-items: center; justify-content: center; gap: 28px; color: var(--brand-blue); font-size: 16px; }
  .contact-item { display: flex; align-items: center; gap: 8px; }
  .contact-item svg { width: 24px; height: 24px; flex: none; }

  .call-band { position: absolute; top: 1117px; left: 0; width: 100%; height: 83px; background: var(--brand-yellow); display: flex; align-items: center; justify-content: center; color: var(--brand-blue); font-style: italic; font-weight: 700; font-size: 36px; letter-spacing: 1px; }
</style>
</head>
<body>
<main class="flyer">
  <header class="brand">
    <span class="brand-name">VENDRICK</span>
    <span class="brand-sub">Contracting</span>
  </header>

  <div class="top-strip"></div>
  <div class="edge-strip"></div>

  <section class="services-band">
    <h1 class="services-title">Our Services</h1>
    <div class="services-rule"></div>
  </section>

  <ul class="service-list">
    <li>Exterior &amp; interior painting</li>
    <li class="gap"></li>
    <li>Framing Repairs</li>
    <li>Siding/Gutters/Windows/Doors</li>
    <li>Concrete Walkways/stoops</li>
    <li>Balcony/Deck Rehab</li>
    <li>Tuckpointing</li>
    <li>Sealants/Caulks</li>
    <li>Pressure Washing</li>
    <li>Specialty Coatings</li>
    <li>Drywall Install/Repair</li>
    <li>Plaster Repairs</li>
    <li>Wallpaper Removal</li>
    <li>Flooring/Tile/Carpet/Hardwood/vinyl</li>
    <li>Leak Investigations:</li>
    <li>Facades, Roofs, Interior Leaks</li>
    <li>EIFS/</li>
    <li>Plumbing Repairs</li>
    <li>Lead Safe Renovations</li>
  </ul>

  <div class="photo-rail"></div>
  <div class="photo photo-saw" role="img" aria-label="Photo of a carpenter cutting a wooden board on a saw"></div>
  <div class="photo photo-tower" role="img" aria-label="Photo of a glass office tower against a blue sky"></div>
  <div class="photo photo-floor" role="img" aria-label="Photo of a worker installing flooring planks"></div>

  <footer class="contact-bar">
    <span class="contact-item">
      <svg viewBox="0 0 24 24"><circle cx="12" cy="12" r="12" fill="#070bac"/><circle cx="12" cy="12" r="6" fill="none" stroke="#fff" stroke-width="1.4"/><ellipse cx="12" cy="12" rx="2.6" ry="6" fill="none" stroke="#fff" stroke-width="1.2"/><line x1="6" y1="12" x2="18" y2="12" stroke="#fff" stroke-width="1.2"/></svg>
      www.vendrickcontracting.com
    </span>
    <span class="contact-item">
      <svg viewBox="0 0 24 24"><circle cx="12" cy="12" r="12" fill="#070bac"/><rect x="6" y="8" width="12" height="8" fill="none" stroke="#fff" stroke-width="1.4"/><polyline points="6,8 12,13 18,8" fill="none" stroke="#fff" stroke-width="1.4"/></svg>
      info@vendrickcontracting
    </span>
    <span class="contact-item">
      <svg viewBox="0 0 24 24"><circle cx="12" cy="12" r="12" fill="#070bac"/><path d="M8.5 6.5l2 2.2-1.2 1.6c.8 1.7 2 2.9 3.7 3.7l1.6-1.2 2.2 2-1.2 1.8c-4.4-.4-8.3-4.3-8.7-8.7z" fill="#fff"/></svg>
      703-555-0148
    </span>
  </footer>

  <div class="call-band">CALL US!</div>
</main>
</body>
</html>
```